Presentation of Business Project of Implementing CRM for a car Detailing Company

We need a professional PowerPoint presentation template (5 slides) for a business presentation about implementing a CRM system at Vantrel Detailing, a premium automotive detailing company in South Africa.
About the Company:
Vantrel Detailing specializes in high-end car detailing, paint protection, leather repair, and classic car restoration. They're a premium service provider looking to modernize their customer management through digital transformation.
What We Need:
A visually impressive presentation template with 5 key slide designs that we can duplicate and reuse across our full presentation. The presentation will show how a ChatLoom-integrated CRM system can help the business grow from 60% to 80% customer retention, free up the owner's time, and enable expansion.
The 5 Slides:

Title slide - Space for project title + 5 team member names (impactful opening)
Content slide - Standard layout with bullet points (we'll duplicate this for 10+ slides)
Large data table - For vendor comparisons (4 rows × 10 columns)
Financial charts - 3 side-by-side scenario comparisons with bar/column charts
Simple table - For cost breakdowns (2-3 columns)

Design Style:
Modern, polished, and eye-catching. Should look professional but capture attention - think sleek automotive industry meets premium business consulting. Bold use of car detailing/workshop imagery as backgrounds where appropriate. Contemporary color scheme. Clean layouts that make data easy to read but NOT boring.

Images:
We will provide a link to high-quality car detailing and workshop images that you can integrate into the design (backgrounds, accents, visual interest).

https://www.filebarrow.example/drive/7kqPz2LmXr9TsWd4Hn3BY-uJE#VantrelDetailing

Link contain image of company actual work and logo of the company. The idea is to use their images.

Important:
All tables and charts should be editable so we can add our own data. Slides should be easy to duplicate and modify.

Deliverables:
5 PowerPoint slides (.pptx) - fully editable
Google Slides version
Fonts/colors consistent throughout

```html
<!DOCTYPE html>
<html lang="en">
<head>
<meta charset="utf-8">
<title>Vantrel Detailing – CRM Presentation Template</title>
<link rel="stylesheet" href="https://fonts.googleapis.com/css2?family=Poppins:wght@400;500;600;700;800&display=swap">
<style>
:root{
  --red:#d7141a;
  --red-soft:#f2a6a6;
  --ink:#1f1f21;
  --dark:#232325;
  --dark-2:#2e2e31;
  --gray-dk:#4a4b50;
  --gray:#7d7e83;
  --gray-lt:#b5b6ba;
  --cell:#c9cacd;
  --white:#ffffff;
  --page:#e8e8e9;
  --band:#c9c9ca;
}
*{box-sizing:border-box;margin:0;padding:0}
html,body{width:1200px;height:2353px;overflow:hidden}
body{background:var(--page);font-family:'Poppins',sans-serif;color:var(--ink);position:relative}
.hero-band{position:absolute;left:0;top:0;width:1200px;height:428px;background:var(--band)}
.slide{position:absolute;width:478px;height:262px;background:var(--white);overflow:hidden;box-shadow:0 14px 22px rgba(0,0,0,.18)}
.slide.dark{background:var(--dark);color:var(--white)}
.photo{position:absolute;background:linear-gradient(135deg,#5b5d63 0%,#2a2b2f 55%,#121214 100%)}
.photo.light{background:linear-gradient(135deg,#d9dadd 0%,#8e9096 50%,#3c3d42 100%)}
.footer-line{position:absolute;left:58px;right:26px;bottom:30px;height:1px;background:var(--red)}
.footer-mark{position:absolute;left:26px;bottom:22px;width:18px;height:18px;border-radius:50%;border:3px solid var(--red);background:var(--gray-lt)}
.dark .footer-mark{background:var(--gray)}
.heading{color:var(--red);font-weight:700;font-size:22px;line-height:1.15}
.lede{font-size:7px;line-height:1.45}
/* title */
.brand{position:absolute;left:30px;top:28px;display:flex;align-items:center;gap:6px}
.brand-dot{width:14px;height:14px;border-radius:50%;background:var(--red)}
.brand-name{font-size:11px;font-weight:600;letter-spacing:1.5px;color:var(--gray-dk)}
.title-kicker{position:absolute;left:24px;top:92px;font-size:20px;font-weight:500}
.title-main{position:absolute;left:22px;top:108px;font-size:50px;font-weight:800;color:var(--red);letter-spacing:-1px}
.title-sub{position:absolute;left:24px;top:176px;width:180px;font-size:8px;line-height:1.5}
.presented{position:absolute;left:24px;bottom:22px;font-size:7px;color:var(--red);font-weight:600}
.presented span{color:var(--ink);font-weight:500}
.web{position:absolute;left:150px;bottom:22px;font-size:8px;color:var(--red);font-weight:500;letter-spacing:.3px;white-space:nowrap}
.web::before{content:"";display:inline-block;width:7px;height:7px;border:1px solid var(--ink);border-radius:50%;margin-right:4px;vertical-align:-1px}
/* team */
.team-copy{position:absolute;left:172px;top:26px;width:282px;font-size:7px;line-height:1.4}
.team-row{position:absolute;left:34px;top:88px;display:flex;gap:14px}
.member{width:72px;height:118px;border-radius:36px;background:var(--gray);position:relative;text-align:center;color:var(--white);padding-top:18px}
.member:nth-child(even){background:var(--gray-dk)}
.member .name{font-size:8px;font-weight:600}
.member .role{font-size:6px}
.member .portrait{position:absolute;left:2px;bottom:0;width:68px;height:68px;border-radius:50%;border:3px solid var(--gray-dk);background:linear-gradient(160deg,#d4d5d8,#7b7c81)}
/* list */
.rail{position:absolute;left:232px;top:26px;width:2px;height:170px;background:var(--red)}
.list{position:absolute;left:224px;top:18px;width:230px}
.list-item{display:flex;gap:8px;margin-bottom:8px}
.icon-ring{flex:none;width:20px;height:20px;border-radius:50%;border:1.5px solid var(--red);background:var(--white);display:flex;align-items:center;justify-content:center}
.icon-ring::after{content:"";width:7px;height:7px;border:1.5px solid var(--red);border-radius:2px}
.list-item h4{font-size:7.5px;font-weight:600}
.list-item p{font-size:6.8px;line-height:1.35}
/* table */
.vendor{position:absolute;left:24px;top:68px;border-collapse:separate;border-spacing:2px;font-size:6px;text-align:center}
.vendor th{font-weight:600;font-size:7px;background:var(--cell);height:13px;width:38px}
.vendor td{background:var(--cell);height:29px;width:38px;line-height:1.2}
.vendor td.row-head{background:var(--red);color:var(--white);font-weight:600;width:28px;border-radius:4px 0 0 4px}
/* chart */
.chart{position:absolute;left:22px;top:70px;width:424px;height:116px}
.chart .grid{stroke:#cfcfd2;stroke-width:.6}
.dark .chart .grid{stroke:#4a4a4e}
.chart text{font-family:'Poppins',sans-serif;font-size:4.5px;fill:var(--ink)}
.dark .chart text{fill:#9a9aa0}
.chart .year{font-size:6px;font-weight:600}
.dark .chart .year{fill:var(--white)}
.b1{fill:var(--gray-dk)}.b2{fill:var(--gray)}.b3{fill:var(--gray-lt)}.b4{fill:var(--red-soft)}
.legend{position:absolute;left:90px;top:196px;display:flex;gap:40px}
.legend-item{display:flex;align-items:center;gap:5px;font-size:6px;line-height:1.1}
.legend-item i{width:20px;height:20px;border-radius:50%;display:block}
/* pricing */
.plans{position:absolute;display:flex;gap:12px}
.plan{width:87px;background:var(--white);position:relative;height:122px;text-align:center}
.dark .plan{background:var(--dark)}
.plan-head{background:var(--gray-dk);color:var(--white);padding:4px 0 4px;font-size:7.5px;line-height:1.2}
.plan-head b{display:block;font-size:11px;font-weight:700}
.plan-head small{font-size:5.5px}
.plan ul{list-style:none;font-size:7px;line-height:1.55;padding-top:6px}
.plan-foot{position:absolute;left:0;right:0;bottom:0;height:22px;background:var(--gray-dk);display:flex;align-items:center;justify-content:center}
.plan-foot span{background:var(--white);color:var(--gray-dk);font-size:7px;font-weight:600;padding:1px 5px;border-radius:2px}
.plan.feature .plan-head,.plan.feature .plan-foot,.plan.feature{background:var(--red)}
.plan.feature{color:var(--white)}
.plan.feature .plan-foot span{color:var(--red)}
.plan.soft .plan-head,.plan.soft .plan-foot{background:var(--gray)}
.plan.soft .plan-foot span{color:var(--gray)}
.dark .plan ul{color:#e5e5e5}
/* features grid */
.features{position:absolute;left:24px;top:88px;display:grid;grid-template-columns:74px 74px;gap:8px 0}
.feature h5{font-size:7.5px;font-weight:600;margin-top:2px}
.feature p{font-size:5.5px;line-height:1.3}
.dark-list{position:absolute;left:245px;top:20px;width:215px;border-left:1px solid #55555a}
.dark-item{display:flex;gap:14px;align-items:center;padding:9px 0 9px 12px;border-bottom:1px solid #55555a}
.dark-item:last-child{border-bottom:none}
.dark-item .icon-ring{background:transparent;border-color:#d5d5d8}
.dark-item .icon-ring::after{border-color:#d5d5d8}
.dark-item h5{font-size:6.5px;font-weight:600}
.dark-item p{font-size:6.5px;line-height:1.3}
.circles{position:absolute;left:24px;top:70px;display:flex;gap:22px}
.circle-card{width:96px;text-align:center}
.circle-card .disc{width:86px;height:86px;margin:0 auto;border-radius:50%;border:3px solid var(--red);box-shadow:0 0 0 4px var(--dark),0 0 0 5px var(--red)}
.circle-card p{font-size:7px;line-height:1.3;margin-top:10px}
.stats{position:absolute;left:22px;top:150px;width:320px;height:66px;background:var(--red);border-radius:12px;transform:skewX(-12deg);display:flex;align-items:center}
.stat{flex:1;text-align:center;transform:skewX(12deg);border-right:1px solid rgba(255,255,255,.55)}
.stat:last-child{border-right:none}
.stat b{display:block;font-size:10px;font-weight:700}
.stat span{font-size:6px;line-height:1.25;display:block}
</style>
</head>
<body>
<div class="hero-band"></div>

<!-- showcase title slide -->
<section class="slide title-slide" style="left:361px;top:83px">
  <svg width="478" height="262" style="position:absolute;left:0;top:0" aria-hidden="true"><path d="M205,0 H236 C226,70 234,120 262,150 L246,160 C214,120 200,60 205,0 Z" fill="var(--red)"/></svg>
  <svg width="478" height="262" style="position:absolute;left:0;top:0" role="img" aria-label="Photo of a black sports car in the detailing studio"><defs><linearGradient id="g0" x1="0" y1="0" x2="1" y2="1"><stop offset="0" stop-color="#6a6c72"/><stop offset=".55" stop-color="#2b2c30"/><stop offset="1" stop-color="#131315"/></linearGradient></defs><path d="M228,0 H478 V262 H445 C335,232 222,145 228,0 Z" fill="url(#g0)"/></svg>
  <div class="brand"><i class="brand-dot"></i><span class="brand-name">VANTREL DETAILING</span></div>
  <div class="title-kicker">PRESENTATION</div>
  <div class="title-main">NAME</div>
  <p class="title-sub">Lorem Ipsum is simply dummy text of the printing and typesetting industry.</p>
  <div class="presented">PRESENTED BY : <span>Name Here</span></div>
  <div class="web">www.vantreldetailing.example</div>
</section>

<!-- 1 title -->
<section class="slide title-slide" style="left:78px;top:464px">
  <svg width="478" height="262" style="position:absolute;left:0;top:0" aria-hidden="true"><path d="M205,0 H236 C226,70 234,120 262,150 L246,160 C214,120 200,60 205,0 Z" fill="var(--red)"/></svg>
  <svg width="478" height="262" style="position:absolute;left:0;top:0" role="img" aria-label="Photo of a black sports car in the detailing studio"><defs><linearGradient id="g1" x1="0" y1="0" x2="1" y2="1"><stop offset="0" stop-color="#6a6c72"/><stop offset=".55" stop-color="#2b2c30"/><stop offset="1" stop-color="#131315"/></linearGradient></defs><path d="M228,0 H478 V262 H445 C335,232 222,145 228,0 Z" fill="url(#g1)"/></svg>
  <div class="brand"><i class="brand-dot"></i><span class="brand-name">VANTREL DETAILING</span></div>
  <div class="title-kicker">PRESENTATION</div>
  <div class="title-main">NAME</div>
  <p class="title-sub">Lorem Ipsum is simply dummy text of the printing and typesetting industry.</p>
  <div class="presented">PRESENTED BY : <span>Name Here</span></div>
  <div class="web">www.vantreldetailing.example</div>
</section>

<!-- 2 team -->
<section class="slide team-slide" style="left:615px;top:464px">
  <h2 class="heading" style="position:absolute;left:25px;top:20px">Our Team<br>Member</h2>
  <p class="team-copy">Lorem Ipsum is simply dummy text of the printing and typesetting industry. Lorem Ipsum has been the industry's standard dummy text ever since the 1500s, when an unknown printer took a galley of type and scrambled it to make a type specimen book.</p>
  <div class="team-row">
    <div class="member"><div class="name">Name Here</div><div class="role">Designation</div><div class="portrait" role="img" aria-label="Team member portrait"></div></div>
    <div class="member"><div class="name">Name Here</div><div class="role">Designation</div><div class="portrait" role="img" aria-label="Team member portrait"></div></div>
    <div class="member"><div class="name">Name Here</div><div class="role">Designation</div><div class="portrait" role="img" aria-label="Team member portrait"></div></div>
    <div class="member"><div class="name">Name Here</div><div class="role">Designation</div><div class="portrait" role="img" aria-label="Team member portrait"></div></div>
    <div class="member"><div class="name">Name Here</div><div class="role">Designation</div><div class="portrait" role="img" aria-label="Team member portrait"></div></div>
  </div>
  <i class="footer-mark"></i><i class="footer-line"></i>
</section>

<!-- 3 content list -->
<section class="slide content-slide" style="left:78px;top:775px">
  <div class="photo" style="left:0;top:0;width:195px;height:115px;border-radius:0 0 26px 0;border-right:3px solid var(--red);border-bottom:3px solid var(--red)" role="img" aria-label="Photo of a sports car rear in the workshop"></div>
  <h2 class="heading" style="position:absolute;left:24px;top:136px">Heading Here</h2>
  <p class="lede" style="position:absolute;left:24px;top:166px;width:160px;text-align:justify">Lorem Ipsum is simply dummy text of the printing and typesetting industry. Lorem Ipsum has been the industry's .</p>
  <i class="rail"></i>
  <div class="list">
    <div class="list-item"><i class="icon-ring"></i><div><h4>LOREM IPSUM 1</h4><p>Lorem Ipsum is simply dummy text of the printing and typesetting industry. Lorem Ipsum has been the industry's .</p></div></div>
    <div class="list-item"><i class="icon-ring"></i><div><h4>LOREM IPSUM 1</h4><p>Lorem Ipsum is simply dummy text of the printing and typesetting industry. Lorem Ipsum has been the industry's .</p></div></div>
    <div class="list-item"><i class="icon-ring"></i><div><h4>LOREM IPSUM 1</h4><p>Lorem Ipsum is simply dummy text of the printing and typesetting industry. Lorem Ipsum has been the industry's .</p></div></div>
    <div class="list-item"><i class="icon-ring"></i><div><h4>LOREM IPSUM 1</h4><p>Lorem Ipsum is simply dummy text of the printing and typesetting industry. Lorem Ipsum has been the industry's .</p></div></div>
  </div>
  <i class="footer-mark"></i><i class="footer-line"></i>
</section>

<!-- 4 vendor table -->
<section class="slide table-slide" style="left:615px;top:775px">
  <h2 class="heading" style="position:absolute;left:0;right:0;top:20px;text-align:center">Vendor Comparisons</h2>
  <table class="vendor">
    <tr><th style="background:none;width:28px"></th><th>Ipsum</th><th>Ipsum</th><th>Ipsum</th><th>Ipsum</th><th>Ipsum</th><th>Ipsum</th><th>Ipsum</th><th>Ipsum</th><th>Ipsum</th><th>Ipsum</th></tr>
    <tr><td class="row-head">Lorem<br>1</td><td>Your text<br>here</td><td>Your text<br>here</td><td>Your text<br>here</td><td>Your text<br>here</td><td>Your text<br>here</td><td>Your text<br>here</td><td>Your text<br>here</td><td>Your text<br>here</td><td>Your text<br>here</td><td>Your text<br>here</td></tr>
    <tr><td class="row-head">Lorem<br>2</td><td>Your text<br>here</td><td>Your text<br>here</td><td>Your text<br>here</td><td>Your text<br>here</td><td>Your text<br>here</td><td>Your text<br>here</td><td>Your text<br>here</td><td>Your text<br>here</td><td>Your text<br>here</td><td>Your text<br>here</td></tr>
    <tr><td class="row-head">Lorem<br>3</td><td>Your text<br>here</td><td>Your text<br>here</td><td>Your text<br>here</td><td>Your text<br>here</td><td>Your text<br>here</td><td>Your text<br>here</td><td>Your text<br>here</td><td>Your text<br>here</td><td>Your text<br>here</td><td>Your text<br>here</td></tr>
    <tr><td class="row-head">Lorem<br>4</td><td>Your text<br>here</td><td>Your text<br>here</td><td>Your text<br>here</td><td>Your text<br>here</td><td>Your text<br>here</td><td>Your text<br>here</td><td>Your text<br>here</td><td>Your text<br>here</td><td>Your text<br>here</td><td>Your text<br>here</td></tr>
  </table>
  <i class="footer-mark"></i><i class="footer-line"></i>
</section>

<!-- 5 chart light -->
<section class="slide chart-slide" style="left:78px;top:1088px">
  <h2 class="heading" style="position:absolute;left:25px;top:20px">Scenario Comparisons Charts</h2>
  <p class="lede" style="position:absolute;left:26px;top:50px">Lorem Ipsum is simply dummy text of the printing and typesetting industry</p>
  <svg class="chart" viewBox="0 0 440 120" aria-label="Grouped bar chart of three scenarios">
    <g class="grid"><line x1="30" x2="440" y1="100" y2="100"/><line x1="30" x2="440" y1="83" y2="83"/><line x1="30" x2="440" y1="66" y2="66"/><line x1="30" x2="440" y1="49" y2="49"/><line x1="30" x2="440" y1="32" y2="32"/><line x1="30" x2="440" y1="15" y2="15"/><line x1="30" x2="440" y1="-2" y2="-2"/><line x1="30" x2="30" y1="-2" y2="100"/></g>
    <g><text x="20" y="101">0</text><text x="17" y="84">20</text><text x="17" y="67">40</text><text x="17" y="50">60</text><text x="17" y="33">80</text><text x="14" y="16">100</text><text x="14" y="0">120</text></g>
    <rect class="b1" x="50" y="30.3" width="15" height="69.7"/><rect class="b2" x="67" y="15" width="15" height="85"/><rect class="b3" x="84" y="83" width="15" height="17"/><rect class="b4" x="101" y="47.3" width="15" height="52.7"/>
    <rect class="b1" x="190" y="67.7" width="15" height="32.3"/><rect class="b2" x="207" y="30.3" width="15" height="69.7"/><rect class="b3" x="224" y="47.3" width="15" height="52.7"/><rect class="b4" x="241" y="15" width="15" height="85"/>
    <rect class="b1" x="330" y="50.7" width="15" height="49.3"/><rect class="b2" x="347" y="35.4" width="15" height="64.6"/><rect class="b3" x="364" y="15" width="15" height="85"/><rect class="b4" x="381" y="49" width="15" height="51"/>
    <text x="53" y="28">82</text><text x="70" y="13">100</text><text x="88" y="81">20</text><text x="104" y="45">62</text>
    <text x="193" y="65">38</text><text x="210" y="28">82</text><text x="227" y="45">62</text><text x="243" y="13">100</text>
    <text x="333" y="48">58</text><text x="350" y="33">76</text><text x="366" y="13">100</text><text x="384" y="47">60</text>
    <text class="year" x="74" y="110">2023</text><text class="year" x="214" y="110">2024</text><text class="year" x="354" y="110">2025</text>
  </svg>
  <div class="legend">
    <div class="legend-item"><i style="background:var(--gray-dk)"></i>Lorem<br>Ipsum</div>
    <div class="legend-item"><i style="background:var(--gray)"></i>Lorem<br>Ipsum</div>
    <div class="legend-item"><i style="background:var(--gray-lt)"></i>Lorem<br>Ipsum</div>
    <div class="legend-item"><i style="background:var(--red-soft)"></i>Lorem<br>Ipsum</div>
  </div>
  <i class="footer-mark"></i><i class="footer-line"></i>
</section>

<!-- 6 chart dark -->
<section class="slide chart-slide dark" style="left:615px;top:1085px;width:489px;height:267px">
  <h2 class="heading" style="position:absolute;left:25px;top:20px">Scenario Comparisons Charts</h2>
  <p class="lede" style="position:absolute;left:26px;top:50px">Lorem Ipsum is simply dummy text of the printing and typesetting industry</p>
  <svg class="chart" viewBox="0 0 440 120" aria-label="Grouped bar chart of three scenarios">
    <g class="grid"><line x1="30" x2="440" y1="100" y2="100"/><line x1="30" x2="440" y1="83" y2="83"/><line x1="30" x2="440" y1="66" y2="66"/><line x1="30" x2="440" y1="49" y2="49"/><line x1="30" x2="440" y1="32" y2="32"/><line x1="30" x2="440" y1="15" y2="15"/><line x1="30" x2="440" y1="-2" y2="-2"/><line x1="30" x2="30" y1="-2" y2="100"/></g>
    <g><text x="20" y="101">0</text><text x="17" y="84">20</text><text x="17" y="67">40</text><text x="17" y="50">60</text><text x="17" y="33">80</text><text x="14" y="16">100</text><text x="14" y="0">120</text></g>
    <rect class="b1" x="50" y="30.3" width="15" height="69.7"/><rect class="b2" x="67" y="15" width="15" height="85"/><rect class="b3" x="84" y="83" width="15" height="17"/><rect class="b4" x="101" y="47.3" width="15" height="52.7"/>
    <rect class="b1" x="190" y="67.7" width="15" height="32.3"/><rect class="b2" x="207" y="30.3" width="15" height="69.7"/><rect class="b3" x="224" y="47.3" width="15" height="52.7"/><rect class="b4" x="241" y="15" width="15" height="85"/>
    <rect class="b1" x="330" y="50.7" width="15" height="49.3"/><rect class="b2" x="347" y="35.4" width="15" height="64.6"/><rect class="b3" x="364" y="15" width="15" height="85"/><rect class="b4" x="381" y="49" width="15" height="51"/>
    <text x="53" y="28">82</text><text x="70" y="13">100</text><text x="88" y="81">20</text><text x="104" y="45">62</text>
    <text x="193" y="65">38</text><text x="210" y="28">82</text><text x="227" y="45">62</text><text x="243" y="13">100</text>
    <text x="333" y="48">58</text><text x="350" y="33">76</text><text x="366" y="13">100</text><text x="384" y="47">60</text>
    <text class="year" x="74" y="110">2023</text><text class="year" x="214" y="110">2024</text><text class="year" x="354" y="110">2025</text>
  </svg>
  <div class="legend">
    <div class="legend-item"><i style="background:var(--gray-dk);border:2px solid var(--red)"></i>Lorem<br>Ipsum</div>
    <div class="legend-item"><i style="background:var(--gray);border:2px solid var(--red)"></i>Lorem<br>Ipsum</div>
    <div class="legend-item"><i style="background:var(--gray-lt);border:2px solid var(--red)"></i>Lorem<br>Ipsum</div>
    <div class="legend-item"><i style="background:var(--red-soft);border:2px solid var(--red)"></i>Lorem<br>Ipsum</div>
  </div>
  <i class="footer-mark"></i><i class="footer-line"></i>
</section>

<!-- 7 cost light -->
<section class="slide cost-slide" style="left:78px;top:1398px">
  <h2 class="heading" style="position:absolute;left:0;right:0;top:20px;text-align:center">Cost Breakdowns</h2>
  <p class="lede" style="position:absolute;left:0;right:0;top:50px;text-align:center">Lorem Ipsum is simply dummy text of the printing and typesetting industry</p>
  <div class="plans" style="left:92px;top:73px">
    <div class="plan" style="border:1px solid #eee"><div class="plan-head">Lorem Ipsum<b>430 zar</b><small>Per Month</small></div><ul><li>Lorem ipsum</li><li>Lorem ipsum</li><li>Lorem ipsum</li><li>Lorem ipsum</li></ul><div class="plan-foot"><span>Get Started</span></div></div>
    <div class="plan feature"><div class="plan-head">Lorem Ipsum<b>540 zar</b><small>Per Month</small></div><ul><li>Lorem ipsum</li><li>Lorem ipsum</li><li>Lorem ipsum</li><li>Lorem ipsum</li></ul><div class="plan-foot"><span>Get Started</span></div></div>
    <div class="plan soft" style="border:1px solid #eee"><div class="plan-head">Lorem Ipsum<b>320 zar</b><small>Per Month</small></div><ul><li>Lorem ipsum</li><li>Lorem ipsum</li><li>Lorem ipsum</li><li>Lorem ipsum</li></ul><div class="plan-foot"><span>Get Started</span></div></div>
  </div>
  <i class="footer-mark"></i><i class="footer-line"></i>
</section>

<!-- 8 cost dark -->
<section class="slide cost-slide dark" style="left:612px;top:1396px;width:482px">
  <div class="photo" style="left:322px;top:0;width:160px;height:262px;border-radius:26px 0 0 0" role="img" aria-label="Photo of a grey sports saloon front in the garage"></div>
  <h2 class="heading" style="position:absolute;left:26px;top:20px">Cost Breakdowns</h2>
  <p class="lede" style="position:absolute;left:27px;top:50px">Lorem Ipsum is simply dummy text of the printing and typesetting industry</p>
  <div class="plans" style="left:26px;top:78px">
    <div class="plan" style="border:1px solid #3a3a3d"><div class="plan-head">Lorem Ipsum<b>430 zar</b><small>Per Month</small></div><ul><li>Lorem ipsum</li><li>Lorem ipsum</li><li>Lorem ipsum</li><li>Lorem ipsum</li></ul><div class="plan-foot"><span>Get Started</span></div></div>
    <div class="plan feature"><div class="plan-head">Lorem Ipsum<b>540 zar</b><small>Per Month</small></div><ul><li>Lorem ipsum</li><li>Lorem ipsum</li><li>Lorem ipsum</li><li>Lorem ipsum</li></ul><div class="plan-foot"><span>Get Started</span></div></div>
    <div class="plan soft" style="border:1px solid #3a3a3d"><div class="plan-head">Lorem Ipsum<b>320 zar</b><small>Per Month</small></div><ul><li>Lorem ipsum</li><li>Lorem ipsum</li><li>Lorem ipsum</li><li>Lorem ipsum</li></ul><div class="plan-foot"><span>Get Started</span></div></div>
  </div>
  <i class="footer-mark"></i><i class="footer-line" style="right:26px"></i>
</section>

<!-- 9 heading with car -->
<section class="slide feature-slide" style="left:78px;top:1704px">
  <svg width="478" height="262" style="position:absolute;left:0;top:0" role="img" aria-label="Photo of a grey estate car in the detailing bay"><defs><linearGradient id="g9" x1="0" y1="0" x2="1" y2="1"><stop offset="0" stop-color="#5d5f65"/><stop offset=".5" stop-color="#2f3034"/><stop offset="1" stop-color="#141416"/></linearGradient></defs><path d="M330,22 C300,30 290,60 292,100 L300,262 H478 V0 Z" fill="url(#g9)"/></svg>
  <h2 class="heading" style="position:absolute;left:24px;top:20px">Heading Here</h2>
  <p class="lede" style="position:absolute;left:24px;top:50px;width:200px;text-align:justify">Lorem Ipsum is simply dummy text of the printing and typesetting industry. Lorem Ipsum has been the industry's standard dummy text ever since the 1500s</p>
  <div class="features">
    <div class="feature"><i class="icon-ring"></i><h5>Lorem Ipsum</h5><p>Lorem Ipsum is simply dummy text of the printing .</p></div>
    <div class="feature"><i class="icon-ring"></i><h5>Lorem Ipsum</h5><p>Lorem Ipsum is simply dummy text of the printing .</p></div>
    <div class="feature"><i class="icon-ring"></i><h5>Lorem Ipsum</h5><p>Lorem Ipsum is simply dummy text of the printing .</p></div>
    <div class="feature"><i class="icon-ring"></i><h5>Lorem Ipsum</h5><p>Lorem Ipsum is simply dummy text of the printing .</p></div>
  </div>
  <i class="footer-mark"></i><i class="footer-line" style="right:180px"></i>
</section>

<!-- 10 heading dark list -->
<section class="slide list-slide dark" style="left:619px;top:1704px">
  <h2 class="heading" style="position:absolute;left:25px;top:20px">Heading Here</h2>
  <div class="photo light" style="left:0;top:60px;width:218px;height:148px;border-radius:0 14px 14px 0" role="img" aria-label="Photo of a white supercar in the studio"></div>
  <div class="dark-list">
    <div class="dark-item"><i class="icon-ring"></i><div><h5>Lorem Ipsum</h5><p>Lorem Ipsum is simply dummy text of the<br>printing and typesetting industry.</p></div></div>
    <div class="dark-item"><i class="icon-ring"></i><div><h5>Lorem Ipsum</h5><p>Lorem Ipsum is simply dummy text of the<br>printing and typesetting industry.</p></div></div>
    <div class="dark-item"><i class="icon-ring"></i><div><h5>Lorem Ipsum</h5><p>Lorem Ipsum is simply dummy text of the<br>printing and typesetting industry.</p></div></div>
    <div class="dark-item"><i class="icon-ring"></i><div><h5>Lorem Ipsum</h5><p>Lorem Ipsum is simply dummy text of the<br>printing and typesetting industry.</p></div></div>
  </div>
  <i class="footer-mark"></i><i class="footer-line"></i>
</section>

<!-- 11 circles dark -->
<section class="slide circles-slide dark" style="left:72px;top:2032px;width:488px;height:267px">
  <h2 class="heading" style="position:absolute;left:0;right:0;top:20px;text-align:center">Heading Here</h2>
  <div class="circles">
    <div class="circle-card"><div class="disc photo light" style="position:relative" role="img" aria-label="Photo of a polished white car panel"></div><p>Lorem Ipsum is simply dummy text of the printing and typesetting industry.</p></div>
    <div class="circle-card"><div class="disc photo light" style="position:relative" role="img" aria-label="Photo of a paint correction close-up"></div><p>Lorem Ipsum is simply dummy text of the printing and typesetting industry.</p></div>
    <div class="circle-card"><div class="disc photo" style="position:relative" role="img" aria-label="Photo of a detailed alloy wheel"></div><p>Lorem Ipsum is simply dummy text of the printing and typesetting industry.</p></div>
    <div class="circle-card"><div class="disc photo" style="position:relative;background:linear-gradient(135deg,#2a2a2d,#8a1216)" role="img" aria-label="Photo of a red leather car interior"></div><p>Lorem Ipsum is simply dummy text of the printing and typesetting industry.</p></div>
  </div>
  <i class="footer-mark"></i><i class="footer-line"></i>
</section>

<!-- 12 stats dark -->
<section class="slide stats-slide dark" style="left:608px;top:2032px;width:489px;height:267px">
  <svg width="489" height="267" style="position:absolute;left:0;top:0" role="img" aria-label="Photo of a detailer steam cleaning a car"><defs><linearGradient id="g12" x1="1" y1="0" x2="0" y2="1"><stop offset="0" stop-color="#9a9ba0"/><stop offset=".5" stop-color="#4a4b50"/><stop offset="1" stop-color="#1c1c1e"/></linearGradient></defs><path d="M300,0 H489 V267 H230 C300,200 280,90 300,0 Z" fill="url(#g12)"/></svg>
  <h2 class="heading" style="position:absolute;left:26px;top:20px">Heading Here</h2>
  <p class="lede" style="position:absolute;left:24px;top:64px;width:206px;text-align:justify">Lorem Ipsum is simply dummy text of the printing and typesetting industry. Lorem Ipsum has been the industry's standard dummy text ever since the 1500s, when an unknown printer took a galley of type and scrambled it to make a type specimen book.</p>
  <div class="stats">
    <div class="stat"><b>250+</b><span>Lorem Ipsum is simply<br>dummy text of the printing<br>and typesetting industry.</span></div>
    <div class="stat"><b>1550+</b><span>Lorem Ipsum is simply<br>dummy text of the printing<br>and typesetting industry.</span></div>
    <div class="stat"><b>450+</b><span>Lorem Ipsum is simply<br>dummy text of the printing<br>and typesetting industry.</span></div>
  </div>
  <i class="footer-mark"></i><i class="footer-line"></i>
</section>
</body>
</html>
```